The Council for Stewardship in Civic Works' 2024 Rise Together Summit: Spark Venture needs a full page flyer that can be converted to a website header.

Date: February, 16, 2024
Location: Harborlight Meeting Pavilion, San Marcos, TX

ABOUT THE FORUM

Dedicated to celebrating the entrepreneurial spirit and unwavering determination of women, the Rise Together Summit proudly presents, “Spark Venture.” Here, we believe in the power of dreams, the strength of innovation, and the impact of women-led endeavors.

Join us at this dynamic Forum as we explore the world of Spark Ventures – those inspiring ventures, including YOURSELF, fueled by creativity, ambition, and a deep-seated love for what we do. Whether you're an seasoned expert, a budding visionary, or simply an enthusiast eager to learn and grow, this Forum is your hub for all things related to the fusion of passion and business.

WHAT TO EXPECT

Inspiring Stories: Immerse yourself in a collection of captivating success stories and personal journeys that highlight the incredible feats achieved through passion-driven initiatives. Learn from remarkable women who turned their dreams into reality and gain insights into their strategies, challenges, and triumphs.

Expert Insights: Discover the art of transforming a passion into a sustainable business model. Our forum gathers experts and thought leaders across the AEC community (and more) to share invaluable advice, practical tips, and proven strategies, guiding you along the exciting journey of pursuing your passion.

Networking Opportunities: Connect with like-minded individuals who share your passion for making a difference. Engage in lively discussions, exchange ideas, and build meaningful relationships with fellow forum participants, potential collaborators, and mentors who can help elevate your Spark Venture.

Interactive Workshops: Participate in hands-on workshops designed to enhance your skills, from refining your business plan to mastering effective marketing techniques. These immersive sessions are tailored to address the unique challenges faced by women in the design and construction industry and will empower you to overcome obstacles with confidence.

Passion Showcase: Elevate your project's visibility by showcasing your Spark Venture to the Forum. Receive feedback, support, and perhaps even connect with individuals who are excited to collaborate and join you on your journey.

Empowerment and Support: Embrace a supportive community that believes in your potential and is committed to fostering an inclusive environment. Share your highs and lows, seek advice, and find encouragement to keep pursuing your passion, no matter the hurdles.

Join Us!

Whether you're taking your first steps toward transforming your passion into a business or are seeking to amplify the impact of your existing venture, or just personal improvement, the Rise Together Summit: "Spark Venture" is your gateway to inspiration, knowledge, and connection. Let's come together, celebrate the strength of women-led endeavors, and empower one another to turn our passions into legacies that shape the future.

Target Market(s)

Professionals in the design and construction industry.

Industry/Entity Type

Design and Construction

Requirements
Must have
• C-SwCW logo
Nice to have
• Title, Date, Location, Graphics that fit the theme of the the Forum: Spark Venture, and the mission of the organization.
Should not have
• Full description of event should be in the graphic.

```html
<!DOCTYPE html>
<html lang="en">
<head>
<meta charset="utf-8">
<title>C-SwCW · 2024 Rise Together Summit · Spark Venture</title>
<link rel="stylesheet" href="https://fonts.googleapis.com/css2?family=Montserrat:wght@500;600;700;800;900&family=Poppins:wght@400;500;600&display=swap">
<style>
  :root {
    --navy: #1f4aa8;
    --navy-deep: #173a8a;
    --green: #7cc242;
    --green-dark: #5aa02c;
    --ink: #2c2f3a;
    --paper: #ffffff;
    --stage: #f1f2f4;
    --photo-light: #e8eef2;
    --photo-mid: #c9d6df;
    --grass: #8fc94f;
  }
  * { box-sizing: border-box; margin: 0; padding: 0; }
  html, body { width: 1200px; height: 2456px; overflow: hidden; background: var(--stage); }
  body { position: relative; font-family: "Poppins", Arial, sans-serif; color: var(--ink); }

  .flyer {
    position: absolute; left: 100px; top: 581px;
    width: 1000px; height: 1294px;
    background: var(--paper);
    overflow: hidden;
    box-shadow: 0 6px 24px rgba(0,0,0,.12);
  }

  .speaker-photo {
    position: absolute; left: 470px; top: 60px; width: 530px; height: 1060px;
    background:
      linear-gradient(180deg, rgba(255,255,255,0) 70%, var(--grass) 88%),
      linear-gradient(160deg, var(--photo-light) 0%, var(--photo-mid) 100%);
  }

  .brand { position: absolute; left: 60px; top: 44px; display: flex; align-items: center; gap: 16px; }
  .brand-mark { width: 64px; height: 64px; background: var(--navy); }
  .brand-name { font-family: "Montserrat", Arial, sans-serif; font-weight: 800; font-size: 44px; color: var(--navy); line-height: 1; }
  .brand-tagline { font-size: 12px; color: var(--ink); margin-top: 6px; letter-spacing: .2px; }

  .headline { position: absolute; left: 60px; top: 170px; font-family: "Montserrat", Arial, sans-serif; }
  .headline-row { display: flex; align-items: center; gap: 18px; }
  .year { font-size: 118px; font-weight: 900; color: var(--navy); line-height: .95; letter-spacing: -2px; }
  .tagline-top { font-size: 46px; font-weight: 800; color: var(--green); line-height: 1; border-bottom: 6px solid var(--green); padding-bottom: 6px; }
  .event-name { font-size: 122px; font-weight: 900; color: var(--navy); line-height: 1; letter-spacing: -2px; margin-top: 4px; }
  .subtitle { display: flex; align-items: center; gap: 14px; margin-top: 10px; }
  .subtitle-label { font-size: 40px; font-weight: 800; color: var(--green); }
  .subtitle-name { font-size: 50px; font-weight: 800; color: var(--navy); line-height: .95; }

  .date-box { position: absolute; left: 60px; top: 560px; border: 4px solid var(--navy); padding: 8px 20px; }
  .date-box p { font-family: "Montserrat", Arial, sans-serif; font-weight: 600; font-size: 46px; color: var(--navy); line-height: 1.1; }
  .venue { position: absolute; left: 60px; top: 650px; font-size: 22px; font-weight: 500; line-height: 1.35; color: var(--ink); }

  .expect { position: absolute; left: 60px; top: 770px; width: 440px; }
  .expect-label { display: inline-block; background: var(--green); color: #fff; font-family: "Montserrat", Arial, sans-serif; font-weight: 800; font-size: 22px; padding: 6px 16px; }
  .expect-grid { list-style: none; display: grid; grid-template-columns: 1fr 1fr; gap: 24px 20px; margin-top: 24px; }
  .expect-grid li { display: flex; align-items: flex-start; gap: 10px; font-size: 20px; font-weight: 600; color: var(--ink); line-height: 1.2; }
  .expect-grid svg { flex: 0 0 22px; margin-top: 2px; }

  .footer-band { position: absolute; left: 0; bottom: 0; width: 1000px; height: 200px; }
  .footer-url { position: absolute; left: 0; bottom: 44px; width: 1000px; text-align: center; font-family: "Montserrat", Arial, sans-serif; font-weight: 700; font-size: 38px; color: #fff; letter-spacing: 5px; }
</style>
</head>
<body>
  <main class="flyer">
    <div class="speaker-photo" role="img" aria-label="Photo of two professional women in business attire walking forward on a green lawn in a bright office setting"></div>

    <header class="brand">
      <div class="brand-mark"></div>
      <div>
        <div class="brand-name">C-SwCW</div>
        <div class="brand-tagline">The Council for Stewardship in Civic Works</div>
      </div>
    </header>

    <section class="headline">
      <div class="headline-row">
        <span class="year">2024</span>
        <span class="tagline-top">RISE<br>TOGETHER</span>
      </div>
      <div class="event-name">SUMMIT</div>
      <div class="subtitle">
        <span class="subtitle-label">FORUM</span>
        <span class="subtitle-name">SPARK<br>VENTURE</span>
      </div>
    </section>

    <div class="date-box"><p>FEBRUARY, 16, 2024</p></div>
    <p class="venue">Harborlight Meeting Pavilion<br>San Marcos, TX</p>

    <section class="expect">
      <span class="expect-label">WHAT TO EXPECT</span>
      <ul class="expect-grid">
        <li><svg width="22" height="22" viewBox="0 0 22 22"><rect width="22" height="22" fill="#1f4aa8"/><path d="M5 11l4 4 8-8" stroke="#fff" stroke-width="3" fill="none"/></svg>Inspiring Stories</li>
        <li><svg width="22" height="22" viewBox="0 0 22 22"><rect width="22" height="22" fill="#1f4aa8"/><path d="M5 11l4 4 8-8" stroke="#fff" stroke-width="3" fill="none"/></svg>Networking Opportunities</li>
        <li><svg width="22" height="22" viewBox="0 0 22 22"><rect width="22" height="22" fill="#1f4aa8"/><path d="M5 11l4 4 8-8" stroke="#fff" stroke-width="3" fill="none"/></svg>Interactive Workshops</li>
        <li><svg width="22" height="22" viewBox="0 0 22 22"><rect width="22" height="22" fill="#1f4aa8"/><path d="M5 11l4 4 8-8" stroke="#fff" stroke-width="3" fill="none"/></svg>Expert Insights</li>
        <li><svg width="22" height="22" viewBox="0 0 22 22"><rect width="22" height="22" fill="#1f4aa8"/><path d="M5 11l4 4 8-8" stroke="#fff" stroke-width="3" fill="none"/></svg>Passion Showcase</li>
        <li><svg width="22" height="22" viewBox="0 0 22 22"><rect width="22" height="22" fill="#1f4aa8"/><path d="M5 11l4 4 8-8" stroke="#fff" stroke-width="3" fill="none"/></svg>Empowerment and Support</li>
      </ul>
    </section>

    <svg class="footer-band" viewBox="0 0 1000 200" preserveAspectRatio="none">
      <path d="M0 40 Q250 10 500 36 T1000 30 V200 H0 Z" fill="#1f4aa8"/>
    </svg>
    <p class="footer-url">www.c-swcw.eventhub.org</p>
  </main>
</body>
</html>
```